依頼詳細
バイクで周辺のニュータウンに配布を考えています。
量販店よりもかなり安いので、安いとわかるようなチラシに仕上げたいです。
また、片面にウォーターサーバーのサブスクの内容を入れてます。
デザインは近いものでイラストを考えています。
記載項目
社名・電話番号・料金プラン
エアコンの取付・取外しをお得にできます。
エアコン基本設置4m 11,000円~
エアコン基本外し 4,000円(2台台以上)
(外し単品は6,000円)
価格は税込み
サイズ
A5
ページ数
片面
希望イメージ
シンプル 複雑
単色 カラフル
暗い 明るい
日常 高級
遊び心 厳粛
未来的 伝統的
女性的 男性的
希望する色
黄・オレンジ系
納品ファイル
• イラストレーター形式 (.ai)
補足説明
■ 選んだ理由

こちらで想定していたのと全然違う構成に感銘を受けました。
かなり手直しが必要ですが、こちらの路線でチラシを作成しようと思います。

■ 提案者全員のお礼・コメント

今回はたくさんのご応募をいただき大変感謝しております。
たくさんのパターンがあり感動しています。
また、同じような応募をしますのでその際はよろしくお願いいたします

```html
<!DOCTYPE html>
<html lang="ja">
<head>
<meta charset="utf-8">
<title>エアコン取付・取外しチラシ</title>
<link rel="stylesheet" href="https://fonts.googleapis.com/css2?family=M+PLUS+1p:wght@500;700;800;900&display=swap">
<style>
:root{
  --yellow:#fdd835;
  --yellow-soft:#ffe873;
  --red:#e8321e;
  --orange:#f39800;
  --ink:#2b2523;
  --white:#ffffff;
  --gray:#5a5350;
}
*{margin:0;padding:0;box-sizing:border-box}
html,body{width:847px;height:1200px;overflow:hidden;background:var(--white)}
body{font-family:"M PLUS 1p",sans-serif;color:var(--ink)}
.flyer{position:relative;width:847px;height:1200px;overflow:hidden;background:var(--white)}
.hero-bg{position:absolute;left:0;top:0;width:847px;height:675px;background:var(--yellow)}
.hero-art{position:absolute;left:0;top:0;width:847px;height:300px;
  background:linear-gradient(180deg,#fff6c4 0%,#fde98a 60%,var(--yellow) 100%)}
.brand{position:absolute;left:14px;top:14px;height:56px;padding:0 20px;background:var(--white);
  border-radius:14px;display:flex;align-items:center;gap:10px;font-weight:800;font-size:28px;color:var(--orange)}
.brand .dot{width:14px;height:14px;border-radius:50%;background:var(--orange)}
.occasion{position:absolute;left:632px;top:24px;width:200px;height:80px;background:var(--white);
  border-radius:40px;display:flex;flex-direction:column;justify-content:center;align-items:center;
  font-weight:800;font-size:20px;line-height:1.3;color:var(--ink)}
.lead{position:absolute;left:0;top:300px;width:847px;text-align:center;font-weight:900;font-size:40px;letter-spacing:1px}
.lead .badge{display:inline-block;background:var(--red);color:var(--white);padding:2px 14px;margin-left:8px;border-radius:6px;transform:translateY(-4px)}
.h-sub{position:absolute;left:0;top:362px;width:847px;text-align:center;font-weight:900;font-size:66px;letter-spacing:2px}
.h-main{position:absolute;left:0;top:438px;width:847px;text-align:center;font-weight:900;font-size:102px;color:var(--red);
  letter-spacing:2px;-webkit-text-stroke:0;text-shadow:5px 5px 0 var(--white),-5px 5px 0 var(--white),5px -5px 0 var(--white),-5px -5px 0 var(--white),0 6px 0 var(--white),6px 0 0 var(--white),0 -6px 0 var(--white),-6px 0 0 var(--white)}
.h-tail{position:absolute;left:0;top:570px;width:847px;text-align:center;font-weight:900;font-size:66px;letter-spacing:2px}
.h-tail .accent{color:var(--red)}
.plan{position:absolute;left:36px;width:780px;height:112px;display:flex;align-items:center}
.plan.install{top:688px}
.plan.remove{top:818px}
.plan-name{width:280px;line-height:1.05;font-weight:900;color:var(--orange)}
.plan-name small{display:block;font-size:30px}
.plan-name strong{display:block;font-size:52px}
.plan-tag{width:78px;height:78px;border-radius:50%;background:var(--orange);color:var(--white);
  display:flex;flex-direction:column;align-items:center;justify-content:center;font-weight:900;font-size:32px;line-height:1;flex:none}
.plan-tag.two{font-size:22px;line-height:1.15}
.plan-price{margin-left:14px;font-weight:900;color:var(--red);font-size:88px;letter-spacing:-1px;line-height:1;white-space:nowrap}
.plan-price .yen{font-size:46px}
.plan-price .tax{font-size:16px;color:var(--ink);letter-spacing:0}
.single-note{position:absolute;left:524px;top:938px;width:274px;height:30px;background:var(--ink);color:var(--white);
  font-weight:700;font-size:18px;display:flex;align-items:center;justify-content:center}
.contact{position:absolute;left:0;top:980px;width:847px;height:220px;background:var(--yellow)}
.contact-line{position:absolute;left:0;top:20px;width:847px;text-align:center;font-weight:800;font-size:28px}
.contact-line .sep{margin:0 18px;color:var(--gray)}
.phone{position:absolute;left:0;top:76px;width:847px;display:flex;justify-content:center;align-items:center;gap:18px}
.phone-icon{width:110px;height:70px}
.phone-number{font-weight:900;font-size:88px;letter-spacing:1px;color:#1d3f8f;line-height:1}
</style>
</head>
<body>
<div class="flyer">
  <div class="hero-bg"></div>
  <div class="hero-art" role="img" aria-label="エアコンを囲んで喜ぶスーツ姿の男女のイラスト"></div>

  <div class="brand"><span class="dot"></span>Solaris</div>
  <div class="occasion"><span>引越しや移設、</span><span>買い替え時に</span></div>

  <p class="lead">量販店よりも<span class="badge">かなりお得!</span></p>
  <h1 class="h-sub">エアコンの</h1>
  <h2 class="h-main">取付・取外し</h2>
  <p class="h-tail"><span class="accent">お得</span>にできます!</p>

  <div class="plan install">
    <div class="plan-name"><small>エアコン</small><strong>基本設置</strong></div>
    <div class="plan-tag">4m</div>
    <div class="plan-price">11,000<span class="yen">円~</span><span class="tax">(税込)</span></div>
  </div>

  <div class="plan remove">
    <div class="plan-name"><small>エアコン</small><strong>基本外し</strong></div>
    <div class="plan-tag two"><span>2台</span><span>以上</span></div>
    <div class="plan-price">4,000<span class="yen">円</span><span class="tax">(税込)</span></div>
  </div>
  <div class="single-note">外し単品 6,000円(税込)</div>

  <div class="contact">
    <p class="contact-line">お問い合せ・お申し込み<span class="sep">|</span>株式会社ソラリス</p>
    <div class="phone">
      <svg class="phone-icon" viewBox="0 0 110 70" aria-hidden="true">
        <rect x="2" y="2" width="106" height="66" rx="10" fill="#1d3f8f"/>
        <path d="M30 46c-6-6-8-14-4-18l6-5 7 8-4 4c2 4 5 7 9 9l4-4 8 7-5 6c-4 4-13 0-21-7z" fill="#fff"/>
        <path d="M66 24h22v6h-15v6h12v6h-12v10h-7z" fill="#fff"/>
      </svg>
      <span class="phone-number">0120-381-275</span>
    </div>
  </div>
</div>
</body>
</html>
```